Business card design needed

I need a business card design for a dog walking, dog minding and dog training business. Please refer to my website for the basic company colours and fonts I'm after. Planning on a double sided card, so all information doesn't need to be on the 'front' side.
Cheers

Industry/Entity Type

Dog Training

Contact Information for Business Card

Meadow Paws - happy hounds
Rua 0498307164
meadowpawsdemo.com.au
-walking
-holiday stays
-onsite care
-training and behavioural consultations

```html
<!DOCTYPE html>
<html lang="en">
<head>
<meta charset="utf-8">
<title>Meadow Paws – Business Card</title>
<link rel="stylesheet" href="https://fonts.googleapis.com/css2?family=Jost:wght@400;500&family=Poiret+One&display=swap">
<style>
  :root {
    --page: #ffffff;
    --card: #f0ebe5;
    --orange: #f05a28;
    --charcoal: #1c1c1c;
    --ink: #1a1a1a;
    --grey-text: #555555;
    --silhouette: #cfcfcf;
  }
  * { margin: 0; padding: 0; box-sizing: border-box; }
  html, body {
    width: 1200px; height: 900px; overflow: hidden;
    background: var(--page);
  }
  .canvas { position: relative; width: 1200px; height: 900px; }
  .card {
    position: absolute; left: 270px; width: 660px; height: 411px;
    background: var(--card);
  }
  .card--front { top: 21px; }
  .card--back { top: 450px; }

  .brand-name {
    position: absolute; left: 0; right: 0; top: 150px;
    text-align: center;
    font-family: "Jost", sans-serif; font-weight: 500;
    font-size: 68px; letter-spacing: 2px;
    color: var(--orange); line-height: 1;
  }
  .tagline {
    position: absolute; left: 0; right: 0; top: 281px;
    text-align: center;
    font-family: "Jost", sans-serif; font-size: 15px;
    color: var(--ink);
  }

  .tab-band {
    position: absolute; left: 0; top: 35px; width: 660px; height: 66px;
    background: var(--orange);
  }
  .tab {
    position: absolute; top: 0; width: 160px; height: 66px;
    background: var(--charcoal); border-radius: 8px;
    display: flex; align-items: center; justify-content: center;
    font-family: "Poiret One", sans-serif; font-size: 27px;
    color: #ffffff; letter-spacing: -0.5px;
  }
  .tab--contact { left: 111px; }
  .tab--services { left: 412px; }

  .walk-scene { position: absolute; left: 55px; top: 165px; }
  .divider {
    position: absolute; left: 356px; top: 144px;
    width: 1px; height: 143px; background: var(--ink);
  }
  .contact-line {
    position: absolute; left: 110px; top: 188px;
    font-family: "Poiret One", sans-serif; font-size: 29px;
    color: var(--ink); white-space: nowrap;
  }
  .contact-name { color: var(--orange); margin-right: 10px; }

  .services-list {
    position: absolute; left: 428px; top: 151px; list-style: none;
    font-family: "Poiret One", sans-serif; font-size: 15px;
    line-height: 17.6px; color: var(--grey-text); letter-spacing: 0.6px;
  }
  .credentials {
    position: absolute; left: 27px; top: 366px;
    font-family: "Jost", sans-serif; font-size: 13px;
    line-height: 16px; color: var(--ink);
  }
</style>
</head>
<body>
<main class="canvas">
  <section class="card card--front">
    <h1 class="brand-name">MEADOW PAWS</h1>
    <p class="tagline">happy hounds.</p>
  </section>

  <section class="card card--back">
    <div class="tab-band">
      <div class="tab tab--contact">CONTACT</div>
      <div class="tab tab--services">SERVICES</div>
    </div>

    <svg class="walk-scene" width="550" height="145" viewBox="0 0 550 145" role="img" aria-label="Grey silhouettes of a walker leading a line of running dogs">
      <defs>
        <linearGradient id="sceneTone" x1="0" y1="0" x2="1" y2="0">
          <stop offset="0" stop-color="#cfcfcf" stop-opacity="0.55"/>
          <stop offset="0.5" stop-color="#d4d4d4" stop-opacity="0.7"/>
          <stop offset="1" stop-color="#cfcfcf" stop-opacity="0.55"/>
        </linearGradient>
      </defs>
      <rect width="550" height="145" rx="10" fill="url(#sceneTone)"/>
    </svg>

    <div class="divider"></div>

    <p class="contact-line"><span class="contact-name">Rua</span>0498307164</p>

    <ul class="services-list">
      <li>Group dog walk</li>
      <li>Group dog walk casual</li>
      <li>Solo dog walk</li>
      <li>Solo dog walk casual</li>
      <li>On site, in home care</li>
      <li>Hound holiday stay</li>
    </ul>

    <p class="credentials">*Meadow Paws is run by a qualified dog behaviourist and trainer who is also an accredited pet first aider.<br>We hold pet care specific public liability insurance and carry a current police check.</p>
  </section>
</main>
</body>
</html>
```